Template for management consulting firm to use with investors

We need a word template design for delivering content to our clients. Our firm evaluates people and talent within a business and then provides information back to our clients. Many of the deliverables are word based. But there are charts, org charts, occasionally graphs (for example feedback scores or ratings), and tables that collate comparative information. The data needs to be clear and clean. Colors need to work for both evaluative information (red/yellow/green) and non-evaluative (dark blue to light blue). We'd like to make sure that we include our logo and be able to create a clean table of contents. Most of the design/text should be black/blue with colors for different sections/content.

Target Market(s)

Private equity investors and CEOs

Font styles to use
Serif

Colors
0667aa
3389bc
86beda
d1f1f4

Requirements
Must have
• Ability to do either horizontal or vertical format
• Cover page that is easy to print and has space for both client name and morrowfield name
• Styles/headings for different levels
• Bullets and quote styles
• Table of contents
• Chart colors
• Header and footer, ideally with way to carry through client name on each page

```html
<!DOCTYPE html>
<html lang="en">
<head>
<meta charset="utf-8">
<title>Morrowfield Partners – Report Template</title>
<link href="https://fonts.googleapis.com/css2?family=Cinzel:wght@400;600;700&family=Lora:ital,wght@0,400;0,600;1,400&family=Open+Sans:wght@400;600&display=swap" rel="stylesheet">
<style>
:root{
  --bg:#000;
  --paper:#fff;
  --navy:#145c8f;
  --blue:#0667aa;
  --mid:#3389bc;
  --light:#86beda;
  --pale:#d1f1f4;
  --grey:#b5b5b5;
  --placeholder:#d3d3d3;
  --ink:#3a3a3a;
  --bar-a:#1b93c4;
  --bar-b:#125f93;
  --bar-c:#6a6a6a;
}
*{box-sizing:border-box;margin:0;padding:0}
html,body{width:1200px;height:843px;overflow:hidden;background:var(--bg)}
body{position:relative;font-family:"Open Sans",sans-serif;color:var(--ink)}
.page{position:absolute;width:282px;height:399px;background:var(--paper);overflow:hidden}
.p1{left:14px;top:14px}.p2{left:314px;top:14px}.p3{left:608px;top:14px}.p4{left:906px;top:14px}
.p5{left:14px;top:427px}.p6{left:314px;top:427px}.p7{left:608px;top:427px}.p8{left:906px;top:427px}

.page-title{position:absolute;left:12px;top:10px;font-family:"Cinzel",serif;font-weight:700;font-size:11.5px;color:var(--navy);letter-spacing:.2px}
.brand-mini{position:absolute;right:7px;top:9px;font-family:"Lora",serif;font-size:5.5px;color:var(--navy)}
.footer-band{position:absolute;left:0;bottom:0;width:100%;height:12px;background:var(--grey)}
.page-num{position:absolute;right:4px;bottom:0;width:15px;height:13px;background:var(--navy);color:#fff;font-size:5px;display:flex;align-items:center;justify-content:center}

.body{font-size:5px;line-height:1.75;color:var(--ink);text-align:justify;overflow:hidden;position:absolute}
.h2{position:absolute;font-family:"Lora",serif;font-weight:600;font-size:9px;color:var(--navy)}
.quote{position:absolute;font-family:"Lora",serif;font-style:italic;font-size:5.6px;line-height:1.55;color:var(--navy)}

.cover-art{position:absolute;left:0;top:0;width:282px;height:286px;background:linear-gradient(150deg,#3d7db3,#2a6aa2 55%,#24639b)}
.cover-title{position:absolute;left:39px;top:154px;font-family:"Cinzel",serif;font-size:19px;color:#fff;letter-spacing:.6px}
.cover-sub{position:absolute;right:42px;top:177px;font-family:"Lora",serif;font-size:7px;color:#fff;text-align:right;line-height:1.5}
.cover-brand{position:absolute;left:0;top:328px;width:282px;text-align:center;font-family:"Lora",serif;font-size:14px;color:var(--navy);letter-spacing:.8px}

.banner{position:absolute;left:0;top:30px;width:282px;height:138px;background:linear-gradient(120deg,#1f6aa3,#0f5a92)}
.banner-text{position:absolute;left:12px;top:122px;width:255px;font-family:"Lora",serif;font-style:italic;font-size:5.7px;line-height:1.65;color:#fff;text-transform:uppercase}

.img-box{position:absolute;left:11px;width:76px;height:81px;border:1px solid var(--navy);display:flex;align-items:center;justify-content:center;font-size:5px;color:var(--navy)}
.icon-title{position:absolute;left:94px;font-family:"Lora",serif;font-size:10px;font-weight:600;color:var(--navy)}

.grey-box{position:absolute;background:var(--placeholder)}

.toc{position:absolute;left:32px;top:53px;width:220px;list-style:none}
.toc li{display:flex;align-items:baseline;font-size:6.3px;color:#333;height:19.5px}
.toc .dots{flex:1;border-bottom:1px dotted #555;margin:0 4px 0 3px}
.toc .pg{width:14px;text-align:right}

.tbl{position:absolute;left:12px;width:256px;border-collapse:collapse;font-size:4.8px;color:#333}
.tbl th{font-weight:600;text-align:left;padding:2px 4px;height:10px}
.tbl td{padding:1.6px 4px}
.tbl.s1 th{border-bottom:1px solid #888}
.tbl.s1{border-bottom:2px solid var(--light)}
.tbl.s2 th{background:#d6d6d6}
.tbl.s2{border-bottom:1px solid #999}
.tbl.s3{border:1px solid var(--navy)}
.tbl.s3 th{background:var(--navy);color:#fff}
.tbl-title{position:absolute;left:12px;font-family:"Lora",serif;color:var(--navy)}
</style>
</head>
<body>

<section class="page p1">
  <div class="cover-art" role="img" aria-label="Blue-toned photo of a business desk with laptop and documents"></div>
  <svg width="282" height="286" style="position:absolute;left:0;top:0">
    <polyline points="41,150 41,127 129,127 129,148" fill="none" stroke="#fff" stroke-width="1.3"/>
    <polyline points="41,180 41,201 129,201" fill="none" stroke="#fff" stroke-width="1.3"/>
  </svg>
  <div class="cover-title">PROJECT TITLE HERE</div>
  <div class="cover-sub">Lorem ipsum dolor sit amet<br>consectetur adipiscing elit</div>
  <div class="cover-brand">MORROWFIELD PARTNERS</div>
  <div class="footer-band"></div>
</section>

<section class="page p2">
  <div class="page-title">BUSINESS TITLE HERE</div>
  <div class="brand-mini">MORROWFIELD</div>
  <div class="banner" role="img" aria-label="Blue-tinted photo of a team meeting"></div>
  <div class="banner-text">Lorem ipsum dolor sit amet, consectetur adipiscing elit, sed do eiusmod tempor incididunt ut labore et dolore magna aliqua. Ut enim ad minim veniam, quis nostrud exercitation ullamco laboris nisi ut aliquip ex ea</div>
  <div class="h2" style="left:13px;top:180px">Lorem ipsum dolor sit amet</div>
  <div class="body" style="left:13px;top:194px;width:124px;height:186px;text-align:left">Lorem ipsum dolor sit amet, consectetur adipiscing elit, sed do eiusmod tempor incididunt ut labore et dolore magna aliqua. Ut enim ad minim veniam, quis nostrud exercitation ullamco laboris nisi ut aliquip ex ea commodo consequat. Duis aute irure dolor in reprehenderit in voluptate velit esse cillum dolore eu fugiat nulla pariatur. Excepteur sint occaecat cupidatat non proident, sunt in culpa qui officia deserunt mollit anim id est laborum."<br><br>"Sed ut perspiciatis unde omnis iste natus error sit voluptatem accusantium doloremque laudantium, totam rem aperiam, eaque ipsa quae ab illo inventore veritatis et quasi architecto beatae vitae dicta sunt explicabo. Nemo enim ipsam voluptatem quia voluptas sit aspernatur aut odit aut fugit, sed quia consequuntur magni dolores eos qui ratione voluptatem sequi nesciunt. Neque porro quisquam est, qui</div>
  <div class="body" style="left:146px;top:194px;width:124px;height:186px;text-align:left">"Lorem ipsum dolor sit amet, consectetur adipiscing elit, sed do eiusmod tempor incididunt ut labore et dolore magna aliqua. Ut enim ad minim veniam, quis nostrud exercitation ullamco laboris nisi ut aliquip ex ea commodo consequat. Duis aute irure dolor in reprehenderit in voluptate velit esse cillum dolore eu fugiat nulla pariatur. Excepteur sint occaecat cupidatat non proident, sunt in culpa qui officia deserunt mollit anim id est laborum."<br><br>"Sed ut perspiciatis unde omnis iste natus error sit voluptatem accusantium doloremque laudantium, totam rem aperiam, eaque ipsa quae ab illo inventore veritatis et quasi architecto beatae vitae dicta sunt explicabo. Nemo enim ipsam voluptatem quia voluptas sit aspernatur aut odit aut fugit, sed quia consequuntur magni dolores eos qui ratione voluptatem sequi nesciunt. Neque porro</div>
  <div class="footer-band"></div><div class="page-num">01</div>
</section>

<section class="page p3">
  <div class="page-title">BUSINESS TITLE HERE</div>
  <div class="brand-mini">MORROWFIELD</div>
  <div class="img-box" style="top:40px">Images</div>
  <div class="icon-title" style="top:36px">Icon Title Here</div>
  <div class="body" style="left:94px;top:50px;width:178px;height:72px">Lorem ipsum dolor sit amet, consectetur adipiscing elit, sed do eiusmod tempor incididunt ut labore et dolore magna aliqua. Ut enim ad minim veniam, quis nostrud exercitation ullamco laboris nisi ut aliquip voluptas nulla pariatur?" Lorem ipsum dolor sit amet, consectetur adipiscing elit, sed do eiusmod tempor incididunt ut labore et dolore magna aliqua. Ut enim ad minim Lorem ipsum dolor sit amet, consectetur adipiscing elit, sed do eiusmod tempor incididunt ut labore et dolore magna aliqua. Ut enim ad minim</div>
  <div class="img-box" style="top:141px">Images</div>
  <div class="icon-title" style="top:137px">Icon Title Here</div>
  <div class="body" style="left:94px;top:151px;width:178px;height:72px">Lorem ipsum dolor sit amet, consectetur adipiscing elit, sed do eiusmod tempor incididunt ut labore et dolore magna aliqua. Ut enim ad minim veniam, quis nostrud exercitation ullamco laboris nisi ut aliquip voluptas nulla pariatur?" Lorem ipsum dolor sit amet, consectetur adipiscing elit, sed do eiusmod tempor incididunt ut labore et dolore magna aliqua. Ut enim ad minim Lorem ipsum dolor sit amet, consectetur adipiscing elit, sed do eiusmod tempor incididunt ut labore et dolore magna aliqua. Ut enim ad minim</div>
  <div class="img-box" style="top:239px">Images</div>
  <div class="icon-title" style="top:235px">Icon Title Here</div>
  <div class="body" style="left:94px;top:249px;width:178px;height:100px">Lorem ipsum dolor sit amet, consectetur adipiscing elit, sed do eiusmod tempor incididunt ut labore et dolore magna aliqua. Ut enim ad minim veniam, quis nostrud exercitation ullamco laboris nisi ut aliquip voluptas nulla pariatur?" Lorem ipsum dolor sit amet, consectetur adipiscing elit, sed do eiusmod tempor incididunt ut labore et dolore magna aliqua. Ut enim ad minim Lorem ipsum dolor sit amet, consectetur adipiscing elit, sed do eiusmod tempor incididunt ut labore et dolore magna aliqua. Ut enim ad minim veniam, quis nostrud exercitation ullamco laboris nisi ut aliquip voluptas nulla pariatur?" Lorem ipsum dolor sit amet, consectetur</div>
  <div class="footer-band"></div><div class="page-num">01</div>
</section>

<section class="page p4">
  <div class="page-title">BUSINESS TITLE HERE</div>
  <div class="brand-mini">MORROWFIELD</div>
  <div class="h2" style="left:13px;top:33px">Lorem ipsum dolor sit amet</div>
  <div class="body" style="left:13px;top:46px;width:258px;height:62px">Lorem ipsum dolor sit amet, consectetur adipiscing elit, sed do eiusmod tempor incididunt ut labore et dolore magna aliqua. Ut enim ad minim veniam, quis nostrud exercitation ullamco laboris nisi ut aliquip ex ea commodo consequat. Duis aute irure dolor in reprehenderit in voluptate velit esse cillum dolore eu fugiat nulla pariatur. Excepteur sint occaecat cupidatat non proident, sunt in culpa qui officia deserunt mollit anim id est laborum." Sed ut perspiciatis unde omnis iste natus error sit voluptatem accusantium doloremque laudantium, totam rem aperiam, eaque ipsa quae ab illo inventore veritatis et quasi architecto beatae vitae dicta sunt explicabo.</div>
  <div class="quote" style="left:13px;top:118px;width:260px">Ut enim ad minima veniam, quis nostrum exercitationem ullam corporis suscipit laboriosam, nisi ut aliquid ex ea commodi consequatur? Quis autem vel eum iure reprehenderit qui in ea voluptate velit esse quam nihil molestiae consequatur, vel illum qui dolorem eum fugiat quo voluptas nulla pariatur?"</div>
  <div class="h2" style="left:13px;top:160px">Lorem ipsum dolor sit amet</div>
  <div class="body" style="left:13px;top:175px;width:124px;height:210px;text-align:left">Lorem ipsum dolor sit amet, consectetur adipiscing elit, sed do eiusmod tempor incididunt ut labore et dolore magna aliqua. Ut enim ad minim veniam, quis nostrud exercitation ullamco laboris nisi ut aliquip ex ea commodo consequat. Duis aute irure dolor in reprehenderit in voluptate velit esse cillum dolore eu fugiat nulla pariatur. Excepteur sint occaecat cupidatat non proident, sunt in culpa qui officia deserunt mollit anim id est laborum."<br><br>"Sed ut perspiciatis unde omnis iste natus error sit voluptatem accusantium doloremque laudantium, totam rem aperiam, eaque ipsa quae ab illo inventore veritatis et quasi architecto beatae vitae dicta sunt explicabo. Nemo enim ipsam voluptatem quia voluptas sit aspernatur aut odit aut fugit, sed quia consequuntur magni dolores eos qui ratione voluptatem sequi nesciunt. Neque porro quisquam est, qui dolorem ipsum quia dolor sit amet, consectetur, adipisci velit, sed quia non numquam eius modi</div>
  <div class="body" style="left:147px;top:175px;width:124px;height:210px;text-align:left">"Lorem ipsum dolor sit amet, consectetur adipiscing elit, sed do eiusmod tempor incididunt ut labore et dolore magna aliqua. Ut enim ad minim veniam, quis nostrud exercitation ullamco laboris nisi ut aliquip ex ea commodo consequat. Duis aute irure dolor in reprehenderit in voluptate velit esse cillum dolore eu fugiat nulla pariatur. Excepteur sint occaecat cupidatat non proident, sunt in culpa qui officia deserunt mollit anim id est laborum."<br><br>"Sed ut perspiciatis unde omnis iste natus error sit voluptatem accusantium doloremque laudantium, totam rem aperiam, eaque ipsa quae ab illo inventore veritatis et quasi architecto beatae vitae dicta sunt explicabo. Nemo enim ipsam voluptatem quia voluptas sit aspernatur aut odit aut fugit, sed quia consequuntur magni dolores eos qui ratione voluptatem sequi nesciunt. Neque porro quisquam est, qui dolorem ipsum quia dolor sit amet, consectetur, adipisci velit, sed quia non numquam</div>
  <div class="footer-band"></div><div class="page-num">01</div>
</section>

<section class="page p5">
  <div class="page-title">BUSINESS TITLE HERE</div>
  <div class="brand-mini">MORROWFIELD</div>
  <div class="h2" style="left:13px;top:35px">Lorem ipsum dolor sit amet</div>
  <div class="body" style="left:13px;top:48px;width:122px;height:136px;text-align:left">Lorem ipsum dolor sit amet, consectetur adipiscing elit, sed do eiusmod tempor incididunt ut labore et dolore magna aliqua. Ut enim ad minim veniam, quis nostrud exercitation ullamco laboris nisi ut aliquip ex ea commodo consequat. Duis aute irure dolor in reprehenderit in voluptate velit esse cillum dolore eu fugiat nulla pariatur. Excepteur sint occaecat cupidatat non proident, sunt in culpa qui officia deserunt mollit anim id est laborum. updatat non proident, sunt in culpa qui officia deserunt mollit anim id est laborum. nim id est laborum. updatat non proident, sunt in culpa qui officia deserunt mollit anim id est laborum.</div>
  <div class="grey-box" style="left:145px;top:42px;width:122px;height:118px"></div>
  <div class="h2" style="left:13px;top:201px">Lorem ipsum dolor sit amet</div>
  <div class="body" style="left:13px;top:214px;width:122px;height:132px;text-align:left">Lorem ipsum dolor sit amet, consectetur adipiscing elit, sed do eiusmod tempor incididunt ut labore et dolore magna aliqua. Ut enim ad minim veniam, quis nostrud exercitation ullamco laboris nisi ut aliquip ex ea commodo consequat. Duis aute irure dolor in reprehenderit in voluptate velit esse cillum dolore eu fugiat nulla pariatur. Excepteur sint occaecat cupidatat non proident, sunt in culpa qui officia deserunt mollit anim id est laborum. updatat non proident, sunt in culpa qui officia deserunt mollit anim id est laborum.</div>
  <div class="grey-box" style="left:145px;top:208px;width:122px;height:118px"></div>
  <div class="footer-band"></div><div class="page-num">01</div>
</section>

<section class="page p6">
  <div class="page-title">BUSINESS TITLE HERE</div>
  <div class="brand-mini">MORROWFIELD</div>
  <ul class="toc">
    <li>Table of Content<span class="dots"></span><span class="pg">01</span></li>
    <li>About US<span class="dots"></span><span class="pg">01</span></li>
    <li>Out Graphs<span class="dots"></span><span class="pg">01</span></li>
    <li>Table of Content<span class="dots"></span><span class="pg">01</span></li>
    <li>Table of Content<span class="dots"></span><span class="pg">01</span></li>
    <li>Table of Content<span class="dots"></span><span class="pg">01</span></li>
    <li>Table of Content<span class="dots"></span><span class="pg">01</span></li>
    <li>Table of Content<span class="dots"></span><span class="pg">01</span></li>
    <li>Table of Content<span class="dots"></span><span class="pg">01</span></li>
    <li>Table of Content<span class="dots"></span><span class="pg">01</span></li>
    <li>Table of Content<span class="dots"></span><span class="pg">01</span></li>
    <li>Table of Content<span class="dots"></span><span class="pg">01</span></li>
    <li>Table of Content<span class="dots"></span><span class="pg">01</span></li>
  </ul>
  <div class="footer-band"></div><div class="page-num">01</div>
</section>

<section class="page p7">
  <div class="page-title">BUSINESS TITLE HERE</div>
  <div class="brand-mini">MORROWFIELD</div>
  <div class="body" style="left:12px;top:46px;width:258px;height:46px">Lorem ipsum dolor sit amet, consectetur adipiscing elit, sed do eiusmod tempor incididunt ut labore et dolore magna aliqua. Ut enim ad minim veniam, quis nostrud exercitation ullamco laboris nisi ut aliquip ex ea commodo consequat. Duis aute irure dolor in reprehenderit in voluptate velit esse cillum dolore eu fugiat nulla pariatur. Excepteur sint occaecat cupidatat non proident, sunt in culpa qui officia deserunt mollit anim id est laborum.</div>
  <div class="tbl-title" style="top:99px;font-size:9.5px;font-weight:600">Table Style 1</div>
  <table class="tbl s1" style="top:115px">
    <tr><th>Title 1</th><th>Title 2</th><th>Title 3</th><th>Title 4</th><th>Title 5</th><th>Title 6</th></tr>
    <tr><td>Lorem ipsum dolor</td><td>xxx</td><td>xxx</td><td>xxx</td><td>xxx</td><td>xxx</td></tr>
    <tr><td>Lorem ipsum dolor</td><td>xxx</td><td>xxx</td><td>xxx</td><td>xxx</td><td>xxx</td></tr>
    <tr><td>Lorem ipsum dolor</td><td>xxx</td><td>xxx</td><td>xxx</td><td>xxx</td><td>xxx</td></tr>
    <tr><td>Lorem ipsum dolor</td><td>xxx</td><td>xxx</td><td>xxx</td><td>xxx</td><td>xxx</td></tr>
  </table>
  <div class="tbl-title" style="top:188px;font-size:6.5px;font-family:'Open Sans',sans-serif;color:#333">Table Style 2</div>
  <table class="tbl s2" style="top:200px">
    <tr><th>Title 1</th><th>Title 2</th><th>Title 3</th><th>Title 4</th><th>Title 5</th><th>Title 6</th></tr>
    <tr><td>Lorem ipsum dolor</td><td>xxx</td><td>xxx</td><td>xxx</td><td>xxx</td><td>xxx</td></tr>
    <tr><td>Lorem ipsum dolor</td><td>xxx</td><td>xxx</td><td>xxx</td><td>xxx</td><td>xxx</td></tr>
    <tr><td>Lorem ipsum dolor</td><td>xxx</td><td>xxx</td><td>xxx</td><td>xxx</td><td>xxx</td></tr>
    <tr><td>Lorem ipsum dolor</td><td>xxx</td><td>xxx</td><td>xxx</td><td>xxx</td><td>xxx</td></tr>
  </table>
  <div class="tbl-title" style="top:272px;font-size:7.5px;font-weight:600">Table Style 3</div>
  <table class="tbl s3" style="top:286px">
    <tr><th>Title 1</th><th>Title 2</th><th>Title 3</th><th>Title 4</th><th>Title 5</th><th>Title 6</th></tr>
    <tr><td>Lorem ipsum dolor</td><td>xxx</td><td>xxx</td><td>xxx</td><td>xxx</td><td>xxx</td></tr>
    <tr><td>Lorem ipsum dolor</td><td>xxx</td><td>xxx</td><td>xxx</td><td>xxx</td><td>xxx</td></tr>
    <tr><td>Lorem ipsum dolor</td><td>xxx</td><td>xxx</td><td>xxx</td><td>xxx</td><td>xxx</td></tr>
    <tr><td>Lorem ipsum dolor</td><td>xxx</td><td>xxx</td><td>xxx</td><td>xxx</td><td>xxx</td></tr>
  </table>
  <div class="footer-band"></div><div class="page-num">01</div>
</section>

<section class="page p8">
  <div class="page-title">BUSINESS TITLE HERE</div>
  <div class="brand-mini">MORROWFIELD</div>
  <div class="h2" style="left:13px;top:33px">Lorem ipsum dolor sit amet</div>
  <div class="body" style="left:13px;top:46px;width:258px;height:36px">Lorem ipsum dolor sit amet, consectetur adipiscing elit, sed do eiusmod tempor incididunt ut labore et dolore magna aliqua. Ut enim ad minim veniam, quis nostrud exercitation ullamco laboris nisi ut aliquip ex ea commodo consequat. Duis aute irure dolor in reprehenderit in voluptate velit esse cillum dolore eu fugiat nulla pariatur. Excepteur sint occaecat cupidatat non proident, sunt in culpa qui officia deserunt mollit anim id est laborum.</div>
  <div class="h2" style="left:13px;top:99px">Lorem ipsum dolor sit amet</div>
  <div class="body" style="left:13px;top:112px;width:258px;height:18px">Lorem ipsum dolor sit amet, consectetur adipiscing elit, sed do eiusmod tempor incididunt ut labore et dolore magna aliqua. Ut enim ad minim veniam sed do eiusmod tempor</div>
  <svg style="position:absolute;left:0;top:0" width="282" height="399">
    <rect x="20" y="168" width="19" height="35" fill="var(--bar-a)"/>
    <rect x="43" y="157" width="19" height="46" fill="var(--bar-a)"/>
    <rect x="66" y="175" width="19" height="28" fill="var(--bar-a)"/>
    <rect x="101" y="177" width="16" height="26" fill="var(--bar-b)"/>
    <rect x="120" y="157" width="16" height="46" fill="var(--bar-b)"/>
    <rect x="139" y="191" width="16" height="12" fill="var(--bar-b)"/>
    <rect x="194" y="167" width="16" height="36" fill="var(--bar-c)"/>
    <rect x="213" y="145" width="16" height="58" fill="var(--bar-c)"/>
    <rect x="232" y="196" width="16" height="7" fill="var(--bar-c)"/>
    <g stroke="#e2e2e2" stroke-width=".5">
      <line x1="58" y1="256" x2="58" y2="359"/><line x1="73" y1="256" x2="73" y2="359"/><line x1="88" y1="256" x2="88" y2="359"/>
      <line x1="103" y1="256" x2="103" y2="359"/><line x1="118" y1="256" x2="118" y2="359"/><line x1="133" y1="256" x2="133" y2="359"/>
      <line x1="148" y1="256" x2="148" y2="359"/><line x1="163" y1="256" x2="163" y2="359"/><line x1="178" y1="256" x2="178" y2="359"/>
      <line x1="193" y1="256" x2="193" y2="359"/><line x1="208" y1="256" x2="208" y2="359"/><line x1="223" y1="256" x2="223" y2="359"/>
      <line x1="58" y1="359" x2="230" y2="359"/>
    </g>
    <g fill="none" stroke-width="1">
      <path d="M58,359 C70,320 80,302 88,298 C110,285 140,270 163,270 C180,270 195,285 208,304" stroke="var(--blue)"/>
      <path d="M58,359 C70,330 78,312 88,312 C110,300 135,280 163,282 C180,284 195,290 208,282" stroke="var(--mid)"/>
      <path d="M58,359 C70,340 80,327 88,322 C110,312 135,302 163,296 C180,290 195,276 208,266" stroke="var(--light)"/>
      <path d="M58,359 C70,345 80,332 88,326 C110,310 135,300 163,322 C180,345 195,335 208,326" stroke="#9a9a9a"/>
      <path d="M58,359 C70,350 80,341 88,340 C110,336 135,356 163,350 C180,330 195,300 208,300" stroke="var(--light)"/>
    </g>
    <g>
      <circle cx="58" cy="359" r="2" fill="var(--bar-b)"/>
      <circle cx="88" cy="298" r="1.8" fill="var(--blue)"/><circle cx="163" cy="270" r="1.8" fill="var(--blue)"/><circle cx="208" cy="304" r="1.8" fill="var(--blue)"/>
      <circle cx="88" cy="312" r="1.8" fill="var(--mid)"/><circle cx="163" cy="282" r="1.8" fill="var(--mid)"/><circle cx="208" cy="282" r="1.8" fill="var(--mid)"/>
      <circle cx="88" cy="322" r="1.8" fill="var(--light)"/><circle cx="163" cy="296" r="1.8" fill="var(--light)"/><circle cx="208" cy="266" r="1.8" fill="var(--light)"/>
      <circle cx="88" cy="326" r="1.8" fill="#9a9a9a"/><circle cx="163" cy="322" r="1.8" fill="#9a9a9a"/><circle cx="208" cy="326" r="1.8" fill="#9a9a9a"/>
      <circle cx="88" cy="340" r="1.8" fill="var(--light)"/><circle cx="163" cy="350" r="1.8" fill="var(--light)"/>
    </g>
  </svg>
  <div class="body" style="left:13px;top:219px;width:258px;height:18px">Lorem ipsum dolor sit amet, consectetur adipiscing elit, sed do eiusmod tempor incididunt ut labore et dolore magna aliqua. Ut enim ad minim veniam sed do eiusmod tempor</div>
  <div class="footer-band"></div><div class="page-num">01</div>
</section>

</body>
</html>
```